Attention grabbing 6x9 postcard

We are looking to have an attention grabbing post card that be sent out to homeowners from our roofing company Olum Roofing. the concept is that on the front it will say something like (STOP THE KNOCKING!
Tired of roofers knocking on your door? Contact us because we value your time as much as you value the roof over your head."
Olum Roofing
OlumRoofing.com
877.612.OLUM
info@olumroofing.com

Please feel free to come up with something very creative. Once we pick the final design we will provide the copy.

```html
<!DOCTYPE html>
<html lang="en">
<head>
<meta charset="utf-8">
<title>Olum Roofing Postcard</title>
<link rel="stylesheet" href="https://fonts.googleapis.com/css2?family=PT+Sans:wght@400;700&display=swap">
<style>
  :root {
    --backdrop: #a8a8a8;
    --honey: #e4b22f;
    --ink: #111111;
    --paper: #ffffff;
    --mail-grey: #dfdfdf;
    --rule: #333333;
    --wood-dark: #6b4321;
    --wood-light: #a9743d;
    --photo-light: #ece9e4;
    --photo-mid: #d9d4cc;
  }
  * { box-sizing: border-box; margin: 0; padding: 0; }
  html, body {
    width: 1200px; height: 2323px; overflow: hidden;
    background: var(--backdrop);
    font-family: "PT Sans", "Trebuchet MS", sans-serif;
    color: var(--ink);
  }
  .postcard {
    position: absolute; top: 756px;
    width: 541px; height: 810px; overflow: hidden;
  }
  /* Front */
  .front { left: 41px; background: var(--honey); }
  .front__photo {
    position: absolute; left: 0; top: 0; width: 100%; height: 351px;
    background: linear-gradient(135deg, var(--wood-light), var(--wood-dark) 55%, var(--wood-light));
  }
  .front__headline {
    position: absolute; left: 0; top: 351px; width: 100%; height: 77px;
    background: var(--paper);
    font-size: 49px; font-weight: 700; letter-spacing: 0.3px;
    display: flex; align-items: center; justify-content: center;
    white-space: nowrap;
  }
  .brand-mark {
    position: absolute; left: 0; top: 446px; width: 100%;
    display: flex; flex-direction: column; align-items: center; gap: 18px;
  }
  .brand-mark__dot {
    width: 60px; height: 60px; border: 3px solid var(--paper); border-radius: 50%;
  }
  .brand-mark__name {
    color: var(--paper); font-size: 14px; letter-spacing: 4px; font-weight: 400;
  }
  .front__question {
    position: absolute; left: 0; top: 568px; width: 100%;
    text-align: center; font-size: 29px;
  }
  .front__question-box {
    position: absolute; left: 32px; top: 608px; width: 478px; height: 54px;
    background: var(--paper);
    display: flex; align-items: center; justify-content: center;
    font-size: 43px; font-weight: 700; white-space: nowrap;
  }
  .front__promise {
    position: absolute; left: 0; top: 688px; width: 100%;
    text-align: center; font-size: 23px; line-height: 28px;
    white-space: nowrap;
  }
  /* Back */
  .back { left: 618px; background: var(--mail-grey); }
  .back__art { position: absolute; left: 0; top: 0; }
  .back__contact {
    position: absolute; left: 281px; top: 82px;
    transform: rotate(90deg); transform-origin: top left;
    white-space: nowrap;
  }
  .back__company { font-size: 44px; font-weight: 700; line-height: 70px; }
  .back__line { font-size: 24px; line-height: 43px; }
  .back__rules { position: absolute; left: 0; top: 0; }
</style>
</head>
<body>

<section class="postcard front">
  <div class="front__photo" role="img" aria-label="Photo of a woman knocking on a wooden front door, seen through a honeycomb frame"></div>
  <h1 class="front__headline">STOP THE KNOCKING!</h1>
  <div class="brand-mark">
    <span class="brand-mark__dot"></span>
    <span class="brand-mark__name">OLUM ROOFING</span>
  </div>
  <p class="front__question">Tired of roofers</p>
  <p class="front__question-box">knocking on your door?</p>
  <p class="front__promise">Contact us because<br>we value your time<br>as much as you value the roof over your head.</p>
</section>

<section class="postcard back">
  <svg class="back__art" width="541" height="810" viewBox="0 0 541 810">
    <defs>
      <linearGradient id="photoTone" x1="0" y1="0" x2="1" y2="1">
        <stop offset="0" stop-color="var(--photo-light)"/>
        <stop offset="1" stop-color="var(--photo-mid)"/>
      </linearGradient>
    </defs>
    <rect x="0" y="0" width="541" height="404" fill="var(--honey)"/>
    <path d="M270 0 Q 200 210 278 404 L541 404 L541 0 Z" fill="var(--paper)"/>
    <path d="M286 0 Q 220 210 292 404 L541 404 L541 0 Z" fill="url(#photoTone)" role="img" aria-label="Photo of a woman in a green shirt knocking on a white door"/>
  </svg>
  <div class="back__contact">
    <p class="back__company">Olum Roofing</p>
    <p class="back__line">OlumRoofing.com</p>
    <p class="back__line">877.612.OLUM</p>
    <p class="back__line">info@olumroofing.com</p>
  </div>
  <svg class="back__rules" width="541" height="810" viewBox="0 0 541 810">
    <g stroke="var(--rule)" stroke-width="1.5">
      <line x1="118" y1="440" x2="118" y2="774"/>
      <line x1="181" y1="440" x2="181" y2="774"/>
      <line x1="247" y1="440" x2="247" y2="774"/>
      <line x1="312" y1="440" x2="312" y2="774"/>
    </g>
    <rect x="392" y="656" width="115" height="116" fill="none" stroke="var(--rule)" stroke-width="1.5"/>
  </svg>
</section>

</body>
</html>
```